PowerPoint Template for Consultancy Company.

We need a Power Point template for a Consultancy company based in Copenhagen, Denmark. We focus on supporting people and small companies in starting up next generation technology companies. Company name is "Vorstrup-Kjær Consulting". The template shall demonstrate growth, agility, next generation technology and following your dreams. Please include the uploaded logo.
Updates
Hi guys,
thanks for helping me on this project.
I like the font "Good Times" that is being used in my logo. I will like this to be used as minimum in the headlines in my power point template. I am not sure if it will work on standard text - but will relay on your judgement.
Kind regards
Torlak
Colors
Designer to choose colors to be used in the design.
Look and feel
Each slider illustrates characteristics of the customer's brand and the style your logo design should communicate.

```html
<!DOCTYPE html>
<html lang="en">
<head>
<meta charset="utf-8">
<title>Timeline – Vorstrup-Kjær Consulting</title>
<link rel="stylesheet" href="https://fonts.googleapis.com/css2?family=Carlito:wght@400;700&display=swap">
<style>
  :root{
    --navy:#0b1f5c;
    --red:#c00000;
    --yellow:#ffff00;
    --deep-blue:#002060;
    --cyan:#00b0f0;
    --grey-text:#7a7a7a;
    --grey-line:#bfbfbf;
    --box-fill:#e8e6e6;
    --white:#ffffff;
  }
  *{margin:0;padding:0;box-sizing:border-box;}
  html,body{width:1200px;height:675px;overflow:hidden;background:var(--white);}
  body{font-family:"Carlito",sans-serif;color:var(--grey-text);}
  .slide{position:relative;width:1200px;height:675px;overflow:hidden;}

  .brand{position:absolute;left:30px;top:38px;display:flex;align-items:center;gap:8px;}
  .brand-mark{width:26px;height:26px;background:var(--navy);}
  .brand-name{font-size:11px;font-weight:700;color:var(--navy);line-height:1.15;letter-spacing:.06em;text-transform:uppercase;}

  .title{position:absolute;left:0;width:1200px;top:50px;text-align:center;font-size:22px;font-weight:700;color:var(--navy);}
  .title-rule{position:absolute;left:577px;top:84px;width:46px;height:3px;background:var(--red);}
  .subheading{position:absolute;left:0;width:1200px;top:96px;text-align:center;font-size:13px;}

  .timeline-art{position:absolute;left:0;top:0;}

  .note{position:absolute;width:157px;height:91px;background:var(--box-fill);border-radius:10px;
        padding:11px 10px;font-size:12.3px;line-height:16.6px;}
  .year{position:absolute;width:76px;height:31px;border:1.5px solid #d0d0d0;border-radius:16px;
        background:var(--white);text-align:center;font-size:17px;font-weight:700;line-height:28px;letter-spacing:.02em;}

  .summary{position:absolute;left:150px;width:900px;top:531px;text-align:center;font-size:13.2px;line-height:24px;}
</style>
</head>
<body>
<main class="slide">
  <header class="brand">
    <span class="brand-mark"></span>
    <span class="brand-name">Vorstrup-Kjær<br>Consulting</span>
  </header>

  <h1 class="title">Timeline</h1>
  <div class="title-rule"></div>
  <p class="subheading">Subheading here</p>

  <svg class="timeline-art" width="1200" height="675" viewBox="0 0 1200 675" aria-hidden="true">
    <defs>
      <filter id="ring-shadow" x="-30%" y="-30%" width="170%" height="170%">
        <feDropShadow dx="2" dy="3" stdDeviation="2.5" flood-color="#000" flood-opacity=".28"/>
      </filter>
    </defs>
    <g stroke="#a6a6a6" stroke-width="1.6" stroke-dasharray="5 2.5">
      <line x1="115" y1="339" x2="340" y2="339"/>
      <line x1="415" y1="339" x2="641" y2="339"/>
      <line x1="716" y1="339" x2="940" y2="339"/>
    </g>
    <g stroke="var(--grey-line)" stroke-width="1" fill="none">
      <polyline points="76,197 76,300"/>
      <polyline points="76,377 76,421 99,441"/>
      <polyline points="402,231 379,251 379,295"/>
      <polyline points="379,370 379,475"/>
      <polyline points="674,197 674,295"/>
      <polyline points="674,370 674,421 697,441"/>
      <polyline points="1010,231 987,251 987,302"/>
      <polyline points="987,377 987,475"/>
    </g>
    <g fill="#bdbdbd">
      <circle cx="78" cy="197" r="4"/>
      <circle cx="381" cy="475" r="4"/>
      <circle cx="675" cy="197" r="4"/>
      <circle cx="988" cy="475" r="4"/>
    </g>
    <g fill="var(--white)" filter="url(#ring-shadow)">
      <circle cx="76" cy="339" r="37"/>
      <circle cx="377" cy="332" r="37"/>
      <circle cx="678" cy="332" r="37"/>
      <circle cx="979" cy="339" r="37"/>
    </g>
    <circle cx="76" cy="339" r="31" fill="var(--yellow)"/>
    <circle cx="377" cy="332" r="31" fill="var(--deep-blue)"/>
    <circle cx="678" cy="332" r="31" fill="var(--cyan)"/>
    <circle cx="979" cy="339" r="31" fill="var(--red)"/>
  </svg>

  <p class="note" style="left:83px;top:205px;">Pellentesque habitant morbi tristique senectus et netus et malesuada fames ac turpis egestas</p>
  <p class="note" style="left:392px;top:374px;">Pellentesque habitant morbi tristique senectus et netus et malesuada fames ac turpis egestas</p>
  <p class="note" style="left:681px;top:205px;">Pellentesque habitant morbi tristique senectus et netus et malesuada fames ac turpis egestas</p>
  <p class="note" style="left:999px;top:374px;">Pellentesque habitant morbi tristique senectus et netus et malesuada fames ac turpis egestas</p>

  <span class="year" style="left:99px;top:427px;">2013</span>
  <span class="year" style="left:402px;top:213px;">2015</span>
  <span class="year" style="left:697px;top:427px;">2017</span>
  <span class="year" style="left:1010px;top:212px;">2019</span>

  <p class="summary">Lorem ipsum dolor sit amet, consectetuer adipiscing elit. Maecenas porttitor congue massa. Fusce posuere, magna sed pulvinar ultricies, purus lectus malesuada libero, sit amet commodo magna eros quis urna.</p>
</main>
</body>
</html>
```